Business Card Design Project

We are a innovative residential building company based in Sydney, Australia
our business name is MARLOWE HOMECRAFT SOLUTIONS PTY LTD.
Our company by line (please incorporate) "Our Business is Building!"
We specialise in creating high end innovative residential Alterations & Additions for our clients.
We would like to see original high end designs that are professional, striking, creative & have the WOW factor...
We like BLACK, BLUE, ORANGE, WHITE, SILVER... We would like to convey to our clients - professionalism/innovative approach/design/creativity/assurance/wow factor...

Target Market(s)

Clients who want/need residential alterations or additions to their homes.

Industry/Entity Type

Residential

Requirements
Must have
• LOGO
Bi Line (somewhere)
Name
Title
Phone number
Email address

Member of the RTA (Regional Trades Assn) Logo
Web Address - www.marlowehomecraft.com.au

Nice to have
• Fantail's are a small New Zealand bird and we would like to incorporate this as part of our new companies (double sided) business card. Whether it be the bird or just it's (fan) tail!
Should not have
• anything old-style.
we are looking for a contemporary, modern & striking Business Cards
clear strong colour accents
we had some stunning designs sent through, our favourites used the birds tail as an imprint on the card (not sure if that is clear of not)

```html
<!DOCTYPE html>
<html lang="en">
<head>
<meta charset="utf-8">
<title>Marlowe Homecraft Solutions – Business Card</title>
<link rel="stylesheet" href="https://fonts.googleapis.com/css2?family=Arimo:wght@400;700&display=swap">
<style>
  :root {
    --page: #cfcfcf;
    --card-white: #ffffff;
    --brand-blue: #1a8fd0;
    --brand-orange: #f47a20;
    --silver: #9a9a9a;
    --back-edge: #e2e2e2;
    --ink-white: #ffffff;
  }
  * { margin: 0; padding: 0; box-sizing: border-box; }
  html, body {
    width: 1200px; height: 1096px; overflow: hidden;
    background: var(--page);
    font-family: "Arimo", Arial, sans-serif;
  }
  .canvas { position: relative; width: 1200px; height: 1096px; }
  .card {
    position: absolute; width: 760px; height: 434px; overflow: hidden;
    box-shadow: 0 4px 14px rgba(0,0,0,0.18);
  }
  .card-front { left: 110px; top: 80px; background: var(--card-white); }
  .card-back {
    left: 330px; top: 590px;
    background: radial-gradient(ellipse at center, #ffffff 0%, #f6f6f6 45%, var(--back-edge) 100%);
  }
  .front-shapes { position: absolute; inset: 0; }
  .fill-blue { fill: var(--brand-blue); }
  .fill-orange { fill: var(--brand-orange); }

  .logo { position: absolute; display: flex; align-items: center; }
  .logo-dot { border-radius: 50%; background: var(--silver); flex: none; }
  .logo-name { color: var(--brand-blue); font-weight: 700; line-height: 1.15; letter-spacing: 0.3px; }
  .card-front .logo { left: 40px; top: 180px; gap: 12px; }
  .card-front .logo-dot { width: 28px; height: 28px; }
  .card-front .logo-name { font-size: 17px; }

  .card-back .brand-lockup {
    position: absolute; left: 0; right: 0; top: 128px;
    display: flex; flex-direction: column; align-items: center; gap: 22px;
  }
  .card-back .logo { position: static; gap: 22px; }
  .card-back .logo-dot { width: 60px; height: 60px; }
  .card-back .logo-name { font-size: 40px; }
  .byline {
    color: var(--silver); font-size: 20px; font-weight: 700; letter-spacing: 0.5px;
  }

  .contact {
    position: absolute; right: 46px; top: 62px; width: 360px;
    text-align: right; color: var(--ink-white);
  }
  .person-name { font-size: 23px; font-weight: 700; }
  .person-title { font-size: 14px; margin-top: 6px; }
  .contact-list { list-style: none; margin-top: 72px; }
  .contact-list li {
    display: flex; justify-content: flex-end; align-items: center; gap: 12px;
    font-size: 16px; margin-bottom: 12px;
  }
  .icon { width: 20px; height: 20px; flex: none; }
  .icon path, .icon rect, .icon circle { fill: none; stroke: var(--ink-white); stroke-width: 1.8; }
  .membership {
    position: absolute; right: 46px; bottom: 30px;
    display: flex; align-items: center; gap: 12px;
    color: var(--ink-white); font-size: 13px;
  }
  .badge { width: 24px; height: 24px; background: var(--ink-white); }
</style>
</head>
<body>
<main class="canvas">

  <section class="card card-front" aria-label="Business card front">
    <svg class="front-shapes" viewBox="0 0 760 434" width="760" height="434" aria-hidden="true">
      <path class="fill-blue" d="M440 0 L760 0 L760 434 L240 434 C360 330 430 180 440 0 Z"/>
      <path class="fill-orange" d="M404 0 L440 0 C430 180 360 330 240 434 C322 328 386 170 404 0 Z"/>
    </svg>

    <div class="logo">
      <span class="logo-dot"></span>
      <span class="logo-name">MARLOWE HOMECRAFT<br>SOLUTIONS PTY LTD.</span>
    </div>

    <div class="contact">
      <p class="person-name">Your Name here</p>
      <p class="person-title">President</p>
      <ul class="contact-list">
        <li>02-5550-0172
          <svg class="icon" viewBox="0 0 20 20" aria-hidden="true"><rect x="6" y="2" width="8" height="16" rx="2"/></svg>
        </li>
        <li>02-5550-0186
          <svg class="icon" viewBox="0 0 20 20" aria-hidden="true"><rect x="3" y="8" width="14" height="8"/><rect x="6" y="3" width="8" height="5"/></svg>
        </li>
        <li>name@marlowehomecraft.com.au
          <svg class="icon" viewBox="0 0 20 20" aria-hidden="true"><rect x="2" y="5" width="16" height="11"/><path d="M2 5 L10 11 L18 5"/></svg>
        </li>
        <li>www.marlowehomecraft.com.au
          <svg class="icon" viewBox="0 0 20 20" aria-hidden="true"><circle cx="10" cy="10" r="8"/><path d="M2 10 H18 M10 2 C6 6 6 14 10 18 M10 2 C14 6 14 14 10 18"/></svg>
        </li>
      </ul>
    </div>

    <div class="membership">
      <span>Member of the RTA</span>
      <span class="badge" role="img" aria-label="Regional Trades Assn membership badge"></span>
    </div>
  </section>

  <section class="card card-back" aria-label="Business card back">
    <div class="brand-lockup">
      <div class="logo">
        <span class="logo-dot"></span>
        <span class="logo-name">MARLOWE HOMECRAFT<br>SOLUTIONS PTY LTD.</span>
      </div>
      <p class="byline">Our Business is Building!</p>
    </div>
  </section>

</main>
</body>
</html>
```